Tall Harbor Business Card

We are a Video Production and Video Equipment Rental company specialising in the supply of state of the art Video Technology and Services for the Live Entertainment, Television and Corporate Business Theatre markets. (in Sydney, Australia) www.tallharbor.example

Industry/Entity Type

Business

Contact Information for Business Card

name, position, email, website, address, logo
Example attached of the information we need - doesn't necessarily have to look the same

Font styles to use
Other font styles liked:
• Tall Harbor logo font is GOTHAM

Colors
ea1f27

Requirements
Nice to have
• either matt black or shiny black cards -
raised logo

```html
<!DOCTYPE html>
<html lang="en">
<head>
<meta charset="utf-8">
<title>Tall Harbor Business Card</title>
<link rel="stylesheet" href="https://fonts.googleapis.com/css2?family=Montserrat:wght@500&family=Oswald:wght@400;500&display=swap">
<style>
  :root {
    --brand-red: #ea1f27;
    --card-black: #0b0b0b;
    --band-white: #ffffff;
    --ink: #141414;
    --backdrop: #e6e6e6;
  }
  * { margin: 0; padding: 0; box-sizing: border-box; }
  html, body { width: 1200px; height: 800px; overflow: hidden; }
  body {
    background: var(--backdrop);
    display: flex;
    align-items: center;
    justify-content: center;
  }
  .business-card {
    position: relative;
    width: 980px;
    height: 560px;
    background: var(--card-black);
    overflow: hidden;
    font-family: "Oswald", "Arial Narrow", sans-serif;
    color: var(--band-white);
    box-shadow: 0 10px 30px rgba(0,0,0,0.25);
  }
  .brand {
    position: absolute;
    left: 80px;
    top: 96px;
    display: flex;
    align-items: center;
    gap: 22px;
  }
  .brand-square {
    width: 22px;
    height: 22px;
    background: var(--brand-red);
  }
  .brand-name {
    font-family: "Montserrat", Arial, sans-serif;
    font-weight: 500;
    font-size: 66px;
    letter-spacing: 1px;
    color: var(--band-white);
    line-height: 1;
    text-transform: uppercase;
  }
  .services {
    position: absolute;
    left: 80px;
    top: 210px;
    font-size: 21px;
    letter-spacing: 1.6px;
    text-transform: uppercase;
    color: var(--band-white);
  }
  .holder {
    position: absolute;
    right: 74px;
    top: 288px;
    text-align: right;
    text-transform: uppercase;
  }
  .holder-name {
    font-size: 34px;
    font-weight: 500;
    letter-spacing: 1.5px;
    color: var(--brand-red);
    line-height: 1.1;
  }
  .holder-role {
    font-size: 19px;
    letter-spacing: 1.4px;
    color: var(--band-white);
    margin-top: 6px;
  }
  .contact-band {
    position: absolute;
    left: 0;
    right: 0;
    top: 375px;
    height: 112px;
    background: var(--band-white);
    color: var(--ink);
    text-transform: uppercase;
  }
  .online {
    position: absolute;
    left: 44px;
    top: 14px;
    list-style: none;
    font-size: 20px;
    letter-spacing: 1.2px;
  }
  .online li {
    display: flex;
    align-items: center;
    gap: 14px;
    height: 38px;
  }
  .online .accent { color: var(--brand-red); }
  .icon { width: 22px; height: 22px; flex: none; }
  .address {
    position: absolute;
    right: 74px;
    top: 16px;
    display: flex;
    align-items: flex-start;
    gap: 16px;
  }
  .address-lines {
    font-style: normal;
    text-align: right;
    font-size: 19px;
    font-weight: 500;
    letter-spacing: 1.2px;
    line-height: 1.3;
  }
  .address .icon { width: 18px; height: 26px; margin-top: 4px; }
</style>
</head>
<body>
  <article class="business-card">
    <header class="brand">
      <span class="brand-square"></span>
      <h1 class="brand-name">Tall Harbor</h1>
    </header>
    <p class="services">Video Solutions - LED Screens - Camera Systems - Projection</p>

    <div class="holder">
      <p class="holder-name">Dane Corvell</p>
      <p class="holder-role">Managing Director</p>
    </div>

    <section class="contact-band">
      <ul class="online">
        <li>
          <span>www.<span class="accent">tallharbor</span>.example</span>
          <svg class="icon" viewBox="0 0 24 24" aria-hidden="true" fill="none" stroke="#ea1f27" stroke-width="1.8">
            <circle cx="12" cy="12" r="10"/>
            <ellipse cx="12" cy="12" rx="4.5" ry="10"/>
            <line x1="2" y1="12" x2="22" y2="12"/>
            <path d="M4 7h16M4 17h16"/>
          </svg>
        </li>
        <li>
          <span>dane@tallharbor.example</span>
          <svg class="icon" viewBox="0 0 24 24" aria-hidden="true">
            <rect x="1" y="5" width="22" height="14" fill="#ea1f27"/>
            <path d="M1 5l11 8 11-8" fill="none" stroke="#ffffff" stroke-width="1.6"/>
          </svg>
        </li>
      </ul>
      <div class="address">
        <address class="address-lines">
          18 Kestrel Lane<br>
          Marlow NSW 2099<br>
          Australia
        </address>
        <svg class="icon" viewBox="0 0 18 26" aria-hidden="true">
          <path d="M9 0C4 0 0 4 0 9c0 7 9 17 9 17s9-10 9-17C18 4 14 0 9 0z" fill="#ea1f27"/>
          <circle cx="9" cy="9" r="3.2" fill="#ffffff"/>
        </svg>
      </div>
    </section>
  </article>
</body>
</html>
```